依頼詳細
■依頼目的
本ブログの目的は、ミラノーヴァ テクノサービシズの認知拡大とブランディングとなります。
MTSの技術や最新動向への見解・取組を掲載する「MTS Tech ブログ」を立ち上げ、
中途採用 転職意向者 / ソリューション導入 検討者の意向を上げることを狙っております。

■デザインイメージ
ポルタリンク社運営ブログ「Buildnotes.XY」
http://dev.portalink-example.jp/
制作注意点としまして、実装にはWordPressを使いますのでWordPressで実装が明らかにできないような
デザインは避けてください

■訴求ポイントの優先順位
1.ブログスペース
2.求人広告バナーエリア(自社のキャリア採用)

■ターゲット層
個人:中途採用 転職意向者
法人:ソリューション導入 検討者

■希望する色味
ミラノーヴァテクノサービシズのトーン&マナーに合わせたもの
http://www.mts.mirano-example.co.jp/

■提供素材
ミラノーヴァテクノサービシズ:ロゴデーター

■納品ファイル
TOPページデザイン1点(PSDデータ)
ロゴの使用につきましては、添付のレギュレーションに従って作成をお願い致します。
デザインコンセプトにつきまして補足をさせて頂きます。TOPページのイメージとしまして一般的なブログ形式ではなく、デザインとレイアウトに関しましては最近のビジネスブログやキュレーションメディアのトレンドも考慮した先進性のあるデザインを考慮し、なおかつ読みやすい体裁での設計をお願いいたします。皆様からのご提案を心よりお待ちしております。よろしくお願いいたします。
ランサー様各位
この度は、たくさんの素晴らしいご提案を頂きましてありがとうございます。
さらにより多くの方からの魅力的なご応募を頂けるのではと思いまして
一週間延長の3/11(水)に延長することといたしました。
引き続き皆様からのご提案をお待ち申し上げます。

サイトの性質上、どうしても縦に長くなる中で、背景色に変化をつけることにより、情報ごとのブロックの認識がわかりやすくなったと感じます。また、単純なグリッドデザインでなくなり、変化がついていたところが決定したポイントになります。

この度は、皆様に当コンペにたくさんの素晴らしいデザインをご提案して頂きましてありがとうございました。

```html
<!DOCTYPE html>
<html lang="ja">
<head>
<meta charset="utf-8">
<title>MTS Tech ブログ</title>
<link href="https://fonts.googleapis.com/css2?family=Noto+Sans+JP:wght@400;700&display=swap" rel="stylesheet">
<style>
:root{
  --blue:#1a8fd6;
  --navy:#1f3f7a;
  --teal:#2eb3c6;
  --sky:#5cc3e6;
  --slate:#8ea4b4;
  --green:#3fae5a;
  --orange:#f08a24;
  --red:#e0493a;
  --gray-bg:#eef1f4;
  --line:#d7dde3;
  --text:#333;
  --muted:#8a949e;
  --white:#fff;
}
*{box-sizing:border-box;margin:0;padding:0}
html,body{width:753px;height:1200px;overflow:hidden}
body{font-family:"Noto Sans JP",sans-serif;color:var(--text);background:var(--white);font-size:8px;line-height:1.4;position:relative}

.topbar{height:95px;position:relative}
.tagline{position:absolute;left:10px;top:6px;font-size:6px;color:var(--muted)}
.brand{position:absolute;display:flex;align-items:center;gap:6px}
.topbar .brand{left:300px;top:34px}
.brand .mark{width:16px;height:16px;background:var(--navy)}
.brand .name{font-size:15px;font-weight:700;color:var(--navy)}
.brand .sub{position:absolute;left:22px;top:22px;font-size:6px;color:var(--muted);white-space:nowrap}
.top-recruit{position:absolute;right:10px;top:10px;display:flex;gap:8px;align-items:flex-start}
.top-recruit .info{font-size:6px;color:var(--muted);line-height:1.5}
.top-recruit .tag{background:var(--blue);color:var(--white);font-size:8px;font-weight:700;padding:6px 10px}

.nav{height:28px;border-top:1px solid var(--line);border-bottom:2px solid var(--blue);display:flex;align-items:center;padding:0 12px;gap:16px}
.nav .logo{font-weight:700;font-size:11px;color:var(--blue);margin-right:4px}
.nav a{font-size:7px;color:var(--text);text-decoration:none}
.nav .search{margin-left:auto;width:120px;height:12px;border:1px solid var(--line)}

.main{position:absolute;top:123px;left:0;width:753px;height:994px;background:var(--gray-bg)}
.posts{position:absolute;left:12px;top:10px;width:550px;display:grid;grid-template-columns:repeat(3,178px);gap:10px 8px}
.card{background:var(--white);height:178px;position:relative;border:1px solid var(--line)}
.thumb{height:66px;position:relative}
.thumb.teal{background:var(--teal)}
.thumb.blue{background:var(--blue)}
.thumb.sky{background:var(--sky)}
.thumb.slate{background:var(--slate)}
.new{position:absolute;left:5px;top:0;background:var(--red);color:var(--white);font-size:5px;font-weight:700;padding:2px 3px}
.title{padding:6px 7px 0;font-size:7.5px;font-weight:700;line-height:1.45;height:30px;overflow:hidden}
.excerpt{padding:4px 7px 0;font-size:6px;color:#666;line-height:1.5;height:33px;overflow:hidden}
.meta{padding:4px 7px 0;font-size:6px;color:var(--muted);display:flex;justify-content:space-between}
.cat{position:absolute;left:0;right:0;bottom:0;height:12px;font-size:6px;color:var(--white);text-align:center;line-height:12px}
.cat.green{background:var(--green)}
.cat.blue{background:var(--blue)}
.cat.teal{background:var(--teal)}
.cat.orange{background:var(--orange)}

.more{position:absolute;left:12px;top:948px;width:550px;height:20px;text-align:center;line-height:20px;font-size:7px;font-weight:700;letter-spacing:1px}

.side{position:absolute;left:572px;top:10px;width:172px}
.side-head{background:var(--blue);color:var(--white);font-size:8px;font-weight:700;padding:4px 7px}
.job{background:var(--white);display:flex;gap:5px;padding:5px;border-bottom:1px solid var(--line)}
.job .pic{width:28px;height:28px;background:#b9c6d1;flex:none}
.job p{font-size:6.5px;line-height:1.4}
.job small{display:block;color:var(--muted);font-size:5.5px}
.banner{margin-top:8px;height:40px;background:var(--white);border:1px solid var(--line);display:flex;align-items:center;gap:6px;padding:0 10px}
.banner .sq{width:12px;height:12px;background:var(--navy)}
.banner .label{font-size:11px;font-weight:700;color:var(--navy)}
.banner.accent .label{color:var(--blue)}
.cats{margin-top:10px;background:var(--white)}
.cats .side-head{background:#333}
.cats li{list-style:none;font-size:7px;padding:3px 8px;border-bottom:1px solid var(--line)}
.cats li::before{content:"› ";color:var(--blue)}
.side-search{margin-top:8px;height:14px;background:var(--white);border:1px solid var(--line)}

.footer{position:absolute;top:1117px;left:0;width:753px;height:83px;background:var(--white)}
.footer .brand{left:250px;top:12px}
.footer .links{position:absolute;left:470px;top:10px;font-size:6.5px;color:var(--muted);line-height:1.8}
.footer .copy{position:absolute;bottom:0;left:0;right:0;height:14px;background:var(--navy);color:var(--white);font-size:6px;text-align:center;line-height:14px}
</style>
</head>
<body>
<header class="topbar">
  <div class="tagline">技術の最新動向をお届けする MTS Tech ブログ</div>
  <div class="brand"><span class="mark"></span><span class="name">ミラノーヴァ</span><span class="sub">テクノサービシズ</span></div>
  <div class="top-recruit">
    <div class="info">タブレット エンジニア 募集<br>業務拡大 中途採用</div>
    <div class="tag">新人募集</div>
  </div>
</header>
<nav class="nav">
  <span class="logo">MTS 技術ブログ</span>
  <a>新着</a><a>人気</a><a>プログラミング</a><a>分析・解析</a><a>モバイル</a><a>タブレット</a><a>その他</a>
  <span class="search"></span>
</nav>

<main class="main">
  <section class="posts">
    <article class="card"><div class="thumb teal" role="img" aria-label="記事のアイキャッチ画像"><span class="new">NEW</span></div><div class="title">Web 開発の効率を高める方法と改善に役立つ6つのポイント</div><div class="excerpt">日々の開発で見落としがちな改善点を整理し、チームで取り組める手順をまとめました。</div><div class="meta"><span>2015.03.10</span><span>山田 太郎</span></div><div class="cat green">PDCA</div></article>
    <article class="card"><div class="thumb teal" role="img" aria-label="記事のアイキャッチ画像"></div><div class="title">数字に仮説を立てるアクセス解析の進め方について</div><div class="excerpt">数値を眺めるだけでなく、仮説を先に置くことで解析の精度が大きく変わります。</div><div class="meta"><span>2015.03.09</span><span>佐藤 花子</span></div><div class="cat blue">分析・解析</div></article>
    <article class="card"><div class="thumb teal" role="img" aria-label="記事のアイキャッチ画像"></div><div class="title">Web 解析で重要な仮説を導き出す基本の視点</div><div class="excerpt">コンサルタントの経験から、仮説づくりに欠かせない視点を三つ紹介します。</div><div class="meta"><span>2015.03.06</span><span>鈴木 一郎</span></div><div class="cat teal">分析・解析</div></article>

    <article class="card"><div class="thumb blue" role="img" aria-label="記事のアイキャッチ画像"></div><div class="title">【CloudNest】Safeport でサブネットを守る手順まとめ</div><div class="excerpt">こんにちは。今回はファイアウォールを使ってサブネットを守る構成を試しました。</div><div class="meta"><span>2015.03.05</span><span>高橋 健</span></div><div class="cat blue">クラウド</div></article>
    <article class="card"><div class="thumb slate" role="img" aria-label="記事のアイキャッチ画像"></div><div class="title">Cumulo Mobile Analytics が Stratus DW 連携に対応</div><div class="excerpt">分析データを自動でエクスポートできるようになりました。設定方法を紹介します。</div><div class="meta"><span>2015.03.04</span><span>伊藤 誠</span></div><div class="cat orange">モバイル</div></article>
    <article class="card"><div class="thumb sky" role="img" aria-label="記事のアイキャッチ画像"></div><div class="title">自社サイトのユーザー行動を分析し改善点を探す</div><div class="excerpt">訪問者の動きを追いかけ、最適な改善点を見つけるための手順を解説します。</div><div class="meta"><span>2015.03.03</span><span>渡辺 涼</span></div><div class="cat teal">クラウド</div></article>

    <article class="card"><div class="thumb teal" role="img" aria-label="記事のアイキャッチ画像"></div><div class="title">PDCA 高速化に繋がる Testkit を用いた画面テスト</div><div class="excerpt">画面テストを自動化し、改善サイクルを短くするための実践例をまとめました。</div><div class="meta"><span>2015.03.02</span><span>山田 太郎</span></div><div class="cat green">PDCA</div></article>
    <article class="card"><div class="thumb teal" role="img" aria-label="記事のアイキャッチ画像"></div><div class="title">Web 解析で重要な仮説を導くサイト設計の考え方</div><div class="excerpt">設計段階から計測を意識することで、後の分析がぐっと楽になります。</div><div class="meta"><span>2015.02.27</span><span>佐藤 花子</span></div><div class="cat blue">分析・解析</div></article>
    <article class="card"><div class="thumb blue" role="img" aria-label="記事のアイキャッチ画像"></div><div class="title">Unison 入門(4) ゲームのオブジェクト操作を学ぶ</div><div class="excerpt">前回に続き、シーン上のオブジェクトを動かす基本的な方法を学びます。</div><div class="meta"><span>2015.02.26</span><span>中村 翔</span></div><div class="cat teal">プログラミング</div></article>

    <article class="card"><div class="thumb teal" role="img" aria-label="記事のアイキャッチ画像"></div><div class="title">第1回 Learning Flare 読書会に参加しました</div><div class="excerpt">社内で開かれた読書会の様子と、議論で出た気づきをまとめて報告します。</div><div class="meta"><span>2015.02.25</span><span>小林 悠</span></div><div class="cat green">タブレット</div></article>
    <article class="card"><div class="thumb teal" role="img" aria-label="記事のアイキャッチ画像"></div><div class="title">PDCA 高速化を進める仮説検証と効果測定の設計</div><div class="excerpt">検証と測定を一つの流れにまとめ、改善を続けるための仕組みを考えます。</div><div class="meta"><span>2015.02.24</span><span>加藤 望</span></div><div class="cat green">PDCA</div></article>
    <article class="card"><div class="thumb teal" role="img" aria-label="記事のアイキャッチ画像"></div><div class="title">アクセス解析で目指すべきゴールを見直すには</div><div class="excerpt">目標設定を見直すことで、成果につながる指標が見えてきます。</div><div class="meta"><span>2015.02.23</span><span>吉田 葵</span></div><div class="cat blue">分析・解析</div></article>

    <article class="card"><div class="thumb sky" role="img" aria-label="記事のアイキャッチ画像"></div><div class="title">データ分析基盤を小さく始めるための構成のコツ</div><div class="excerpt">最小構成から始めて、必要に応じて拡張していく考え方を紹介します。</div><div class="meta"><span>2015.02.20</span><span>山本 剛</span></div><div class="cat teal">分析・解析</div></article>
    <article class="card"><div class="thumb blue" role="img" aria-label="記事のアイキャッチ画像"></div><div class="title">クラウド環境でのバックアップ自動化を試してみた</div><div class="excerpt">定期バックアップを自動で回す仕組みを作り、運用の手間を減らしました。</div><div class="meta"><span>2015.02.19</span><span>高橋 健</span></div><div class="cat blue">クラウド</div></article>
    <article class="card"><div class="thumb slate" role="img" aria-label="記事のアイキャッチ画像"></div><div class="title">モバイルアプリの通知設計で離脱を防ぐ工夫</div><div class="excerpt">通知の頻度と内容を見直し、利用者の離脱を減らした事例をまとめます。</div><div class="meta"><span>2015.02.18</span><span>伊藤 誠</span></div><div class="cat orange">モバイル</div></article>
  </section>

  <div class="more">MORE ▾</div>

  <aside class="side">
    <div class="side-head">新人募集</div>
    <div class="job"><div class="pic" role="img" aria-label="求人イメージ写真"></div><p>タブレット エンジニア<small>業務拡大 中途採用 2015.03.10</small></p></div>
    <div class="job"><div class="pic" role="img" aria-label="求人イメージ写真"></div><p>Web アプリケーションエンジニア<small>自社サービス開発 2015.03.05</small></p></div>
    <div class="job"><div class="pic" role="img" aria-label="求人イメージ写真"></div><p>Web アプリケーションエンジニア<small>受託開発チーム 2015.03.01</small></p></div>
    <div class="banner"><span class="sq"></span><span class="label">ミラノーヴァ</span></div>
    <div class="banner accent"><span class="label">REGI+</span></div>
    <div class="banner accent"><span class="label">JINZAI-Desk</span></div>
    <div class="banner"><span class="label">MTS 技術ブログ</span></div>
    <div class="cats">
      <div class="side-head">カテゴリー</div>
      <ul>
        <li>新着</li><li>人気</li><li>プログラミング</li><li>分析・解析</li><li>モバイル</li><li>タブレット</li><li>クラウド</li><li>その他</li>
      </ul>
    </div>
    <div class="side-search"></div>
  </aside>
</main>

<footer class="footer">
  <div class="brand"><span class="mark"></span><span class="name">ミラノーヴァ</span><span class="sub">テクノサービシズ</span></div>
  <div class="links">運営会社について<br>お問い合わせ<br>MTS 技術ブログについて</div>
  <div class="copy">© ミラノーヴァ テクノサービシズ</div>
</footer>
</body>
</html>
```